Rise As Captain Book Cover Design

Book Cover Design Brief
Book Title
Rise As Captain
Subtitle
The 10 Quiet Habits of Remarkable Command
Author
Orwen Dalquist
Overview
This book is about leadership that starts within.
Most leadership books focus on tactics or management strategies. This book focuses on the inner disciplines that create powerful leaders — mindset, integrity, focus, empathy, professionalism, honesty, and self-respect.
The tone of the book is bold, direct, confident, and transformational.
This is not a soft or corporate leadership book. It is a call to step up and become the leader you are capable of becoming.
The cover should feel:
• Powerful
• Professional
• Transformational
• Premium
• Memorable
Think best-selling leadership book, not a generic business book.
Target Audience
Business owners
Managers
Entrepreneurs
Team leaders
Professionals who want to grow as leaders
Most readers are ambitious professionals who want to level up their leadership and life.
Design Direction
The design should communicate:
Strength. Discipline. Leadership. Personal transformation.
Avoid cliché leadership visuals like:
• Handshakes
• Office buildings
• Corporate stock imagery
• Teams sitting around tables
The design should feel iconic, bold, and timeless.
Think about covers of successful leadership books such as:
Copper Rituals
Total Stewardship
Won't Break Now
Begin From Purpose
The 36 Rules of Sway
These covers are simple, powerful, and recognizable even at small sizes.
Typography
The title RISE AS CAPTAIN should be:
• Bold
• Strong
• Dominant on the cover
• Easy to read even at small sizes (important for Vellora thumbnails)
The subtitle should be clean and secondary to the title.
The overall typography should feel strong, modern, and premium.
Color Direction
Designers are free to explore colors, but the cover should feel strong and premium, not playful.
Colors that often work well for leadership books include:
Black
Gold
White
Deep blue
Dark red
High contrast and clarity are important.
Style
Preferred style:
• Clean
• Modern
• Minimal
• Strong contrast
Avoid clutter and overly busy designs.
The goal is to create a cover that feels powerful and professional at first glance.
Deliverables
Front cover design for a leadership book.
Final files should include:
• High resolution artwork
• Editable source files
• Print-ready version suitable for publishing
Goal of the Cover
When someone sees this book on Vellora or in a bookstore, they should immediately think:
“This looks like a serious leadership book.”
The design should feel like it belongs next to books by authors such as:
Marcus Thorley
Brandt Osgood
Peter Hollis
Nolan Fairbrook
A strong, confident cover that attracts leaders who want to grow and perform at a higher level.
Target Market(s)
Business Owners and High level managers
Look and feel
Each slider illustrates characteristics of the customer's brand and the style your logo design should communicate.

```html
<!DOCTYPE html>
<html lang="en">
<head>
<meta charset="utf-8">
<title>Rise As Captain — Front Cover</title>
<link rel="stylesheet" href="https://fonts.googleapis.com/css2?family=Montserrat:wght@700;800;900&display=swap">
<style>
  :root {
    --stage: #353535;
    --paper: #fcf1ed;
    --ink: #0b0b0b;
    --accent: #ff3d00;
    --on-accent: #fff6ef;
  }
  * { box-sizing: border-box; margin: 0; padding: 0; }
  html, body {
    width: 1200px;
    height: 1200px;
    overflow: hidden;
    background: var(--stage);
  }
  .stage {
    width: 1200px;
    height: 1200px;
    display: flex;
    align-items: center;
    justify-content: center;
  }
  .front-cover {
    position: relative;
    width: 620px;
    height: 1100px;
    background: var(--paper);
    font-family: "Montserrat", sans-serif;
    color: var(--ink);
  }
  .subtitle-badge {
    position: absolute;
    top: 40px;
    left: 76px;
    width: 218px;
    height: 218px;
    border-radius: 50%;
    background: var(--accent);
    color: var(--on-accent);
    display: flex;
    align-items: center;
    justify-content: center;
    text-align: center;
    font-weight: 800;
    font-size: 22px;
    line-height: 1.2;
    letter-spacing: -0.02em;
    text-transform: uppercase;
    padding: 0 22px;
  }
  .author-name {
    position: absolute;
    top: 62px;
    right: 44px;
    font-weight: 800;
    font-size: 30px;
    letter-spacing: -0.03em;
  }
  .title {
    position: absolute;
    right: 44px;
    bottom: 110px;
    text-align: right;
    font-weight: 900;
    text-transform: uppercase;
    line-height: 0.9;
    letter-spacing: -0.03em;
  }
  .title-line { display: block; }
  .title-line--lead { font-size: 176px; }
  .title-line--accent {
    font-size: 118px;
    color: var(--accent);
    margin-top: 12px;
  }
</style>
</head>
<body>
  <main class="stage">
    <section class="front-cover" aria-label="Rise As Captain front cover">
      <p class="subtitle-badge">The 10 Quiet Habits of Remarkable Command</p>
      <p class="author-name">Orwen Dalquist</p>
      <h1 class="title">
        <span class="title-line title-line--lead">Rise</span>
        <span class="title-line title-line--lead">As</span>
        <span class="title-line title-line--accent">Captain</span>
      </h1>
    </section>
  </main>
</body>
</html>
```